Web Design Project: Facility Management company

Hi! We need a new website.

Our current website: http://www.vireo-trade.ru/ and we don-t like it. =)
The structure of our company has changed and now we don't need "cleaning" and "engeneering" on this site.

We are facility management company in Russia. So we provide integrated service solutions specific to industrial services: maintenance, repair, etc. of engineering systems.
More services:
Energy planning
Automation
Audit
Statements with regulators
Video surveillance
Central heating
Security systems
Welding
Management of subcontractors
Electrical installation and service needs
Reception
Catering

Visitors:
* Managers in the field of commercial real estate
* Chief engineers
* TOP managers of large companies, malls, factories...
+ their subordinates
* Small% of applicants.

Here you can see some websites/patterns we liked:
http://www.kobalmire.ru/ (This is our competitor’s site, so our site shouldn’t be an exact copy))))
http://www.dwatqo.ru/
http://www.layoutfarrow.com/demo/24296.html
http://www.layoutfarrow.com/website-templates/10145.html

Style:
Light, hi-tech/minimalizm, the color palette should be based on the original site colors (Green + black + white). http://www.vireo-trade.ru/

Estimated sitemap:
1. Home
2. About Us
3. Company's policy
4. History + Achievements.
5. Certificates
6. Map of presence (Here you can use sample map in file "our projects")
7. Services
8. Portfolio
9. News or blog
10. Jobs
11. Contacts - with the feedback form (or the function "call to order")
12. English

Need a design pages: main page, page 404. The rest of the page could be created by general pattern.

Logo, navigation bar and contacts should be visible on all pages of a site.
Flash animation elements and buttons, etc. - not needed.

* We need to develop 3 websites, so we are looking for a long term cooperation.
Looking forward to your creativity =)

Must Have:
Clear, intuitive structure of web pages.
In the center - of pictures reflecting our main services (industrial theme). May be in rotation.
BUT! This banner (central picture) should not be a huge one =)
All relevant information should be visible at once without scrolling.

A possibility to place media files (presentations, video ...) and 2 banner links on the main page.

Font should be available in Cyrillic.
Updates

IMPORTANT!

Please notice that in thisdesign we don't need "cleaning" and "engeneering" on this site.

So don't use old block of 4pictures from our current website. We don't need it anymore. 

Thestructure of our company has changed and now we need some links (may be banners,may be something else) to our future cleaning website as well as engeneeringwebsite.
It should look like seperate (partner) companies, not like our sevices.

Regards, Vera.

Please don't forget that we need bilingual site.

So define language changing tool in your designs.

Industry/Entity Type

Industrial

```html
<!DOCTYPE html>
<html lang="en">
<head>
<meta charset="utf-8">
<title>Vireo Service — Facility Management</title>
<link href="https://fonts.googleapis.com/css2?family=Open+Sans:wght@300;400;600;700&family=Oswald:wght@500&family=Michroma&display=swap" rel="stylesheet">
<style>
:root{
  --green:#9fc03a;
  --green-dark:#86a82a;
  --black:#111;
  --nav-text:#9a9a9a;
  --text:#555;
  --heading:#1a1a1a;
}
*{margin:0;padding:0;box-sizing:border-box}
html,body{width:1107px;height:1200px;overflow:hidden}
body{position:relative;background:#fff;font-family:"Open Sans",Arial,sans-serif;color:var(--text);font-size:10.5px}
.abs{position:absolute}
.topbar{left:0;top:0;width:1107px;height:43px;background:linear-gradient(#3a3a3a,#262626);border-bottom:1px solid #555}
.lang{left:124px;top:15px;color:#bbb;font-size:11px;display:flex;align-items:center;gap:8px}
.phone{left:790px;top:5px;color:#fff;font-family:"Oswald",sans-serif;font-size:24px;display:flex;align-items:center;gap:8px;letter-spacing:-.5px}
.nav{left:0;top:43px;width:1107px;height:84px;background:linear-gradient(#1d1d1d,#0c0c0c)}
.nav a{position:absolute;color:var(--nav-text);text-decoration:none;font-size:13px;font-weight:600;letter-spacing:-.2px}
.nav a.active{color:#fff}
.nav .sep{position:absolute;top:18px;width:1px;height:48px;background:#333}
.nav .rule{position:absolute;top:41px;height:1px;border-top:1px dotted #3c3c3c}
.brand{left:0;top:127px;width:1107px;height:129px;background:linear-gradient(#fff,#f6f6f6)}
.brand-name{position:absolute;left:418px;top:46px;display:flex;align-items:center;gap:10px;font-size:26px;font-weight:300;color:#1a1a1a;letter-spacing:3px}
.brand-name i{display:block;width:16px;height:16px;background:var(--green)}
.banner-band{left:0;top:256px;width:1107px;height:303px;background:var(--green)}
.banner-frame{left:121px;top:256px;width:864px;height:303px;background:#fff}
.banner-photo{left:126px;top:256px;width:855px;height:303px;background:linear-gradient(160deg,#cfcfcf 0%,#9a9a9a 40%,#4a4a4a 75%,#222 100%)}
.tag{position:absolute;background:#1a1a1a;color:#fff;letter-spacing:-1px;white-space:nowrap}
.tag b{color:var(--green);font-weight:400}
.tag1{left:477px;top:345px;font-size:24px;padding:0 10px;height:31px;line-height:31px}
.tag2{left:644px;top:389px;font-size:18px;padding:0 10px;height:29px;line-height:29px}
.mid{left:0;top:559px;width:1107px;height:299px;background:linear-gradient(#fafafa,#e6e6e6)}
.services-title{left:127px;top:590px;color:var(--green);font-size:21px;font-weight:600;letter-spacing:-.5px}
.intro{left:129px;top:629px;font-size:11px;font-weight:300;color:#444}
.services{left:130px;top:652px;list-style:none}
.services li{font-size:10.5px;font-weight:300;color:#444;height:18.7px;padding-left:18px;position:relative;white-space:nowrap}
.services li::before{content:"";position:absolute;left:0;top:2px;border-left:11px solid var(--green);border-top:4px solid transparent;border-bottom:3px solid transparent;transform:skewY(-20deg)}
.vdiv{width:1px;border-left:1px dotted #bbb}
.btn{position:absolute;height:20px;padding:0 8px;background:linear-gradient(#fafafa,#e4e4e4);border:1px solid #d6d6d6;color:#444;font-size:10.5px;font-weight:600;line-height:18px;white-space:nowrap}
.btn::before{content:"› "}
.welcome-title{left:556px;top:585px;font-family:"Michroma",sans-serif;font-weight:400;font-size:27px;line-height:30px;color:#111;letter-spacing:-2px}
.welcome p{font-size:10.9px;font-weight:300;color:#555;line-height:17px;margin-bottom:9px}
.welcome{left:518px;top:627px;width:456px}
h3{position:absolute;font-size:20px;font-weight:600;color:var(--heading);letter-spacing:-.5px}
.news-item{position:absolute;left:128px;width:235px;height:60px;border-bottom:1px dotted #bbb}
.date{position:absolute;left:0;top:0;width:37px;height:40px;background:#1a1a1a;color:#fff;text-align:center;font-size:15px;font-weight:700;line-height:18px;padding-top:3px}
.date span{display:block;font-size:10px;font-weight:400;color:#aaa;line-height:12px}
.date::after{content:"";position:absolute;left:12px;bottom:-6px;border-left:6px solid transparent;border-right:6px solid transparent;border-top:6px solid #1a1a1a}
.news-item h4{position:absolute;left:44px;top:-2px;color:var(--green);font-size:11.5px;font-weight:600;white-space:nowrap}
.news-item p{position:absolute;left:44px;top:15px;font-size:10.5px;font-weight:300;color:#666;white-space:nowrap}
.video{left:408px;top:925px;width:301px;height:190px;background:#111;padding:6px}
.video-fill{width:100%;height:100%;background:linear-gradient(135deg,#ddd,#8a8a8a 55%,#3a3a3a);position:relative}
.contact{left:753px;top:922px;font-size:10.5px;color:#222;line-height:15.5px;font-style:normal}
.contact .k{color:var(--green-dark);display:inline-block;width:38px}
.footer{left:0;top:1146px;width:1107px;height:54px;background:linear-gradient(#2a2a2a,#111)}
.footer p{position:absolute;left:128px;top:24px;color:#777;font-size:10.5px;font-weight:300}
</style>
</head>
<body>

<header>
  <div class="abs topbar">
    <div class="abs lang">Select Your Language:
      <svg width="20" height="14" viewBox="0 0 20 14" aria-label="English"><rect width="20" height="14" fill="#1f3f8f"/><path d="M0 0L20 14M20 0L0 14" stroke="#fff" stroke-width="3"/><path d="M0 0L20 14M20 0L0 14" stroke="#c8102e" stroke-width="1"/><path d="M10 0V14M0 7H20" stroke="#fff" stroke-width="4"/><path d="M10 0V14M0 7H20" stroke="#c8102e" stroke-width="2"/></svg>
      <svg width="20" height="14" viewBox="0 0 20 14" aria-label="Русский"><rect width="20" height="5" fill="#fff"/><rect y="5" width="20" height="4" fill="#1c4fc4"/><rect y="9" width="20" height="5" fill="#d52b1e"/></svg>
    </div>
    <div class="abs phone">
      <svg width="26" height="26" viewBox="0 0 24 24"><path d="M6.6 10.8a15 15 0 0 0 6.6 6.6l2.2-2.2c.3-.3.7-.4 1-.2 1.1.4 2.3.6 3.6.6.6 0 1 .4 1 1V20c0 .6-.4 1-1 1A17 17 0 0 1 3 4c0-.6.4-1 1-1h3.5c.6 0 1 .4 1 1 0 1.3.2 2.5.6 3.6.1.3 0 .7-.2 1z" fill="#777"/></svg>
      +7 812 400 3186
    </div>
  </div>
  <nav class="abs nav">
    <svg style="position:absolute;left:171px;top:22px" width="6" height="9"><path d="M0 0L6 4.5L0 9z" fill="#9fc03a"/></svg>
    <a class="active" style="left:183px;top:20px">HOME</a>
    <a style="left:183px;top:49px">ABOUT US</a>
    <a style="left:320px;top:20px">COMPANY'S POLICY</a>
    <a style="left:320px;top:49px">HISTORY</a>
    <a style="left:510px;top:20px">CERTIFICATES</a>
    <a style="left:510px;top:49px">Map OF PRESENCE</a>
    <a style="left:695px;top:20px">SERVICES</a>
    <a style="left:695px;top:49px">PORTFOLIO</a>
    <a style="left:849px;top:20px">NEWS/ BLOG</a>
    <a style="left:849px;top:49px">JOBS</a>
    <span class="sep" style="left:280px"></span><span class="sep" style="left:476px"></span><span class="sep" style="left:653px"></span><span class="sep" style="left:805px"></span>
    <span class="rule" style="left:183px;width:85px"></span><span class="rule" style="left:320px;width:140px"></span><span class="rule" style="left:510px;width:130px"></span><span class="rule" style="left:695px;width:95px"></span><span class="rule" style="left:849px;width:125px"></span>
  </nav>
  <div class="abs brand">
    <div class="brand-name"><i></i>VIREO SERVICE</div>
  </div>
</header>

<section>
  <div class="abs banner-band"></div>
  <div class="abs banner-frame"></div>
  <div class="abs banner-photo" role="img" aria-label="Black and white photo of construction scaffolding and cranes against a cloudy sky"></div>
  <div class="tag tag1"><b>Commercial</b> Real Estate Management</div>
  <div class="tag tag2"><b>Integrated</b> Operation of Real Estate</div>
</section>

<main>
  <div class="abs mid"></div>
  <h2 class="abs services-title">OUR SERVICES</h2>
  <p class="abs intro">Our own team of professionals organize and provide:</p>
  <ul class="abs services">
    <li>Management of commercial real estate</li>
    <li>Operation of commercial real estate</li>
    <li>Operation of industrial hazardous sites</li>
    <li>Operation and maintenance of plants and factories</li>
    <li>Maintenance of industrial and production equipment</li>
    <li>Maintenance of engineering systems and equipment of any complexity</li>
    <li>Design and installation of engineering systems</li>
    <li>Reconstruction and modernization of systems engineering</li>
  </ul>
  <a class="btn" style="left:146px;top:811px">read more</a>

  <div class="abs vdiv" style="left:497px;top:590px;height:240px"></div>

  <svg class="abs" style="left:516px;top:585px" width="32" height="32" viewBox="0 0 32 32"><circle cx="16" cy="16" r="14" fill="none" stroke="#9fc03a" stroke-width="3"/><circle cx="16" cy="16" r="9" fill="#9fc03a"/></svg>
  <h2 class="abs welcome-title">WELCOME!</h2>
  <div class="abs welcome">
    <p>We work with you for 8 years. At one time we were one of the first who decided to develop an integrated operation of real estate in Russia. Today we employ more than 500 professionals in the business portfolio of the dozens of projects ranging from small to super regional bank branch mall. creating a company, we have set a goal to get priceless knowledge: what our client wants. Now we can say with confidence that, at least, closer to your desires, and we are ready to listen together to build a mutually beneficial business.</p>
    <p>More and more businesses today - the owners and the companies - developers assigning the operation of buildings with all the engineering equipment is outsourced to professional management company.</p>
  </div>
  <a class="btn" style="left:516px;top:811px">read more</a>

  <h3 style="left:127px;top:876px">NEW &amp; EVENTS</h3>
  <div class="news-item" style="top:925px"><div class="date">15<span>Apr</span></div><h4>Lorem ipsum dolor sit amet</h4><p>consectetuer adipiscing elit, sed diam ....</p></div>
  <div class="news-item" style="top:985px"><div class="date">03<span>Apr</span></div><h4>Lorem ipsum dolor sit amet</h4><p>consectetuer adipiscing elit, sed diam ....</p></div>
  <div class="news-item" style="top:1045px;border:0"><div class="date">01<span>Apr</span></div><h4>Lorem ipsum dolor sit amet</h4><p>consectetuer adipiscing elit, sed diam ....</p></div>
  <a class="btn" style="left:170px;top:1095px">read more</a>

  <div class="abs vdiv" style="left:392px;top:925px;height:195px"></div>
  <h3 style="left:416px;top:876px">PRESENTATIONS</h3>
  <div class="abs video">
    <div class="video-fill" role="img" aria-label="Video still of a business presentation in a meeting room">
      <svg style="position:absolute;left:104px;top:46px" width="84" height="84" viewBox="0 0 84 84"><circle cx="42" cy="42" r="40" fill="#e6e6e6" stroke="#bbb" stroke-width="2"/><path d="M33 28L58 42L33 56z" fill="#111"/></svg>
    </div>
  </div>
  <div class="abs vdiv" style="left:725px;top:925px;height:195px"></div>

  <svg class="abs" style="left:753px;top:876px" width="30" height="30" viewBox="0 0 30 30"><circle cx="15" cy="15" r="13" fill="none" stroke="#9fc03a" stroke-width="3"/><circle cx="15" cy="15" r="8" fill="#9fc03a"/></svg>
  <h3 style="left:795px;top:876px">CONTACT US</h3>
  <address class="abs contact">
    Legal address: 191020, St. Petersburg,<br>ul. Lesnaya, 14<br>Postal address: 196110, St. Petersburg,<br>Kamennaya, 7<br><br>
    <span class="k">Phone:</span>+7 812 400 31 86<br>
    <span class="k">Fax:</span>+7 812 471 58 23<br><br>
    <span class="k">E-mail:</span>mail@vireo-trade.ru.
  </address>
  <a class="btn" style="left:752px;top:1095px;letter-spacing:.3px">Click Here to View Map</a>
</main>

<footer class="abs footer">
  <p>© Vireoservice 2012. All right reserved.</p>
</footer>

</body>
</html>
```